Labour Day banner showcasing 20% off site

Banner graphic promoting our Labour Day sale
Size: 2000px x 600px
- examples from other companies and their sale banners have been uploaded for inspiration. Labour day examples are for the United States's holiday and submissions should NOT be in their country colours.
- product images can be found at www.tallpinegreens.com

Target Market(s)

19+

Industry/Entity Type

Cannabis

Requirements
Must have
• Phrases:
- “Happy Labour Day”
- “20% off site wide sale*"
- "Coupon code: Harvest20"
- Underneath phrase the date of sale “September 3rd - 7th”
- In tiny print “*excludes all sale and bundled items”
- MUST BE 2000px x 600px
Nice to have
• - images of the products or bud we carry which can be found at www.tallpinegreens.com
- bold
Should not have
• - company logo
- the American flag, we are a Canadian company, colours and flag should all be Canadian

```html
<!DOCTYPE html>
<html lang="en">
<head>
<meta charset="utf-8">
<title>Happy Labour Day Sale Banner</title>
<link rel="stylesheet" href="https://fonts.googleapis.com/css2?family=Montserrat:ital,wght@0,600;0,800;1,500;1,800&family=Lilita+One&display=swap">
<style>
  :root {
    --page: #f5f5f5;
    --white: #ffffff;
    --red: #ed1c24;
    --red-dark: #c81b22;
    --red-light: #f0433f;
    --maroon: #7a1518;
    --blue: #1a7fc6;
    --blue-dark: #0f5fa8;
    --sky: #2bb8ea;
    --grey: #d4d4d6;
    --ink: #111111;
  }
  * { margin: 0; padding: 0; box-sizing: border-box; }
  html, body { width: 1200px; height: 1000px; overflow: hidden; background: var(--page); }
  .canvas { position: relative; width: 1200px; height: 1000px; }
  .banner {
    position: absolute; left: 41px; top: 312px; width: 1118px; height: 335px;
    overflow: hidden; background: var(--white);
  }
  .banner-shapes { position: absolute; inset: 0; }
  .flags-art {
    position: absolute; left: 225px; top: 330px; width: 290px; height: 180px;
    border-radius: 40px 40px 10px 10px;
    background: linear-gradient(180deg, #f2f2f2 0%, #e84a4a 60%, #d32a2a 100%);
  }
  .greeting-ribbon {
    position: absolute; left: 250px; top: 470px; width: 230px; height: 84px;
    background: var(--red); border: 3px solid var(--maroon);
    border-radius: 0 0 110px 110px / 0 0 40px 40px;
    display: flex; flex-direction: column; align-items: center; justify-content: center;
    font-family: "Lilita One", sans-serif; color: var(--white); line-height: 1;
    text-align: center;
  }
  .greeting-ribbon .line-one { font-size: 30px; letter-spacing: 1px; }
  .greeting-ribbon .line-two { font-size: 24px; letter-spacing: 1px; }
  .product-lineup {
    position: absolute; left: 185px; top: 582px; width: 375px; height: 58px;
    border-radius: 4px;
    background: linear-gradient(90deg, #5a2a6a 0%, #b88a2a 30%, #7a3aa0 45%, #222 58%, #e8e020 75%, #2a3a6a 90%, #2a9a4a 100%);
    opacity: .85;
  }
  .sale-block { position: absolute; left: 503px; top: 325px; }
  .date-tab {
    position: absolute; left: 0; top: 16px; width: 260px; height: 48px;
    background: linear-gradient(90deg, var(--blue-dark), var(--sky));
    transform: rotate(-5deg); transform-origin: left top;
    font: italic 800 20px "Montserrat", sans-serif; color: var(--white);
    display: flex; align-items: center; justify-content: center;
    border-radius: 3px;
  }
  .offer-box {
    position: absolute; left: 28px; top: 40px; width: 360px; height: 150px;
    background: linear-gradient(90deg, #2b86d6, var(--blue-dark));
    transform: rotate(-4deg); transform-origin: left top;
    border-radius: 4px;
    display: flex; flex-direction: column; align-items: center; justify-content: center;
    font-family: "Montserrat", sans-serif; font-weight: 800; color: var(--white); line-height: 1;
  }
  .offer-box .headline { font-size: 52px; }
  .offer-box .subline { font-size: 30px; margin-top: 4px; }
  .coupon {
    position: absolute; left: 627px; top: 571px;
    font: 600 20px "Montserrat", sans-serif; color: var(--ink); letter-spacing: .3px;
  }
  .coupon .code { color: var(--red); font-weight: 800; }
  .fine-print {
    position: absolute; left: 736px; top: 619px;
    font: italic 500 13px "Montserrat", sans-serif; color: var(--white);
  }
</style>
</head>
<body>
<div class="canvas">
  <div class="banner">
    <svg class="banner-shapes" width="1118" height="335" viewBox="0 0 1118 335" aria-hidden="true">
      <polygon points="335,0 1118,0 1118,335 567,335" fill="var(--red)"/>
      <polygon points="700,0 1118,0 1118,335 860,335" fill="var(--red-light)" opacity=".35"/>
      <polygon points="335,0 470,0 640,240 567,335" fill="var(--red-dark)" opacity=".5"/>
      <polygon points="515,245 545,245 606,335 567,335" fill="var(--grey)"/>
      <path d="M520,238 H890 Q925,238 956,298 H555 Z" fill="var(--white)"/>
      <path d="M22,190 H100 Q120,190 150,240 H70 Q50,240 22,190 Z" fill="var(--red)"/>
      <path d="M0,284 H80 Q115,284 140,335 H0 Z" fill="var(--red-dark)"/>
      <path d="M740,22 q8,-6 16,0 t16,0 t16,0 t16,0 t16,0" fill="none" stroke="var(--white)" stroke-width="1.5"/>
      <path d="M740,32 q8,-6 16,0 t16,0 t16,0 t16,0 t16,0" fill="none" stroke="var(--white)" stroke-width="1.5"/>
      <path d="M690,208 q8,-6 16,0 t16,0 t16,0 t16,0 t16,0" fill="none" stroke="var(--white)" stroke-width="1.5"/>
      <path d="M875,78 l8,8 M883,78 l-8,8 M848,198 l8,8 M856,198 l-8,8" stroke="var(--white)" stroke-width="1.5"/>
    </svg>
    <div class="product-lineup" role="img" aria-label="Row of product packages: lotions, honey jar, sprays, tin and pouches" style="left:144px;top:270px;"></div>
  </div>
  <div class="flags-art" role="img" aria-label="Two crossed Canadian flags on poles"></div>
  <div class="greeting-ribbon">
    <span class="line-one">HAPPY</span>
    <span class="line-two">LABOUR DAY</span>
  </div>
  <div class="sale-block">
    <div class="offer-box">
      <span class="headline">20% Off</span>
      <span class="subline">site wide sale</span>
    </div>
    <div class="date-tab">September 3rd - 7th</div>
  </div>
  <p class="coupon">COUPON CODE: <span class="code">HARVEST20</span></p>
  <p class="fine-print">*excludes all sale and bundled items</p>
</div>
</body>
</html>
```